Webdesign mit Wordpress DIVI Theme - CI und Logo vorhanden
Zielgruppe
Wir veranstalten eine Messe zum Thema Reinigung von Zügen und Straßenbahnen. Die Webseite soll folgende Zielgruppen ansprechen:
* Aussteller (Reinigungsindustrie)
* Besucher
* Presse
Aufgabenstellung
Wir brauchen ein Wordpress Deisgn basierend auf dem DIVI Theme!
Erwartet wird ein fertiges Layout mit Divi gemacht, welches wir importieren können.
Es gibt bereits einen Styleguide und ein Logo. Diese sind angehängt. Bitte entsprechend berücksichtigen.

```html
<!DOCTYPE html>
<html lang="de">
<head>
<meta charset="utf-8">
<title>Tramwash Forum – Messe 2019</title>
<link href="https://fonts.googleapis.com/css2?family=Prompt:wght@300;400;500;600&display=swap" rel="stylesheet">
<style>
:root{
  --stage:#cbc9ca;
  --teal:#1f5a6b;
  --slate:#456a7a;
  --slate-dark:#3d5662;
  --ink:#2e5668;
  --orange:#e09a00;
  --ice:#d9ecf3;
  --night:#1d242c;
  --footer:#242526;
  --muted:#7c9aa6;
  --white:#fff;
}
*{box-sizing:border-box;margin:0;padding:0}
html,body{width:1200px;height:3731px;overflow:hidden}
body{background:var(--stage);font-family:"Prompt",sans-serif;color:var(--ink);position:relative}
.page{position:absolute;left:116px;top:68px;width:968px;height:3589px;background:var(--white);overflow:hidden}
.abs{position:absolute}
.c{text-align:center}
.wordmark{font-weight:500;color:var(--white);line-height:1.05;text-align:center}
.nav{position:absolute;top:41px;left:568px;display:flex;gap:16px;font-size:7px;font-weight:600;color:#222;letter-spacing:.3px}
.btn{display:inline-block;font-size:7px;padding:3px 9px;background:var(--slate);color:var(--white);letter-spacing:.6px}
.btn.light{background:var(--white);color:var(--slate)}
.small{font-size:7px;line-height:12px;color:var(--muted);font-weight:300}
.card{position:absolute;color:var(--white);text-align:center;padding:14px 12px}
.card h4{font-weight:500;font-size:11px;line-height:11px;margin-bottom:6px}
.card p{font-size:6.5px;line-height:11px;opacity:.8;font-weight:300;margin-bottom:8px}
.card .sub{font-size:6px;font-weight:600;opacity:1;margin-bottom:6px}
.dots{font-size:7px;letter-spacing:2px}
.field{position:absolute;background:var(--white);height:20px;font-size:6px;color:#888;padding:5px 7px}
.acc{position:absolute;left:96px;width:775px;height:20px;background:var(--ice);font-size:7px;padding:6px 7px;color:var(--ink)}
.acc::after{content:"";position:absolute;right:8px;top:7px;width:5px;height:5px;border-radius:50%;background:var(--ink)}
</style>
</head>
<body>
<main class="page">

  <!-- Header -->
  <header>
    <div class="abs" style="left:264px;top:0;width:95px;height:96px;background:var(--teal);display:flex;align-items:center;justify-content:center">
      <div class="wordmark" style="font-size:15px">Tramwash<br>Forum</div>
    </div>
    <nav class="nav"><span>AUSSTELLER</span><span>BESUCHER</span><span>PRESSE</span></nav>
  </header>

  <!-- Hero -->
  <section class="abs" style="left:0;top:62px;width:968px;height:370px">
    <div role="img" aria-label="Foto eines einfahrenden Zuges mit Lichtspuren im U-Bahnhof" class="abs" style="inset:0;background:linear-gradient(100deg,#2a2f38 0%,#6d7680 35%,#e9e4ea 55%,#3b3a52 70%,#15161d 100%)"></div>
    <svg class="abs" style="left:0;top:0" width="968" height="370" viewBox="0 0 968 370">
      <path d="M0 353 C300 340 650 320 968 303 L968 370 L0 370Z" fill="var(--orange)"/>
      <path d="M0 370 C300 352 650 335 968 325 L968 370Z" fill="var(--white)"/>
    </svg>
    <div class="abs c" style="left:284px;top:74px;width:400px;color:var(--white)">
      <h1 style="font-size:17px;font-weight:500;margin-bottom:6px">Your Title Goes Here</h1>
      <p style="font-size:7px;line-height:12px;font-weight:300">Your content goes here. Edit or remove this text inline or in the module Content settings.<br>You can also style every aspect of this content in the module Design settings and even<br>apply custom CSS to this text in the module Advanced settings.</p>
      <span class="btn" style="margin-top:8px">Click Here</span>
    </div>
  </section>

  <!-- Messe 2019 -->
  <section>
    <h2 class="abs c" style="left:0;width:968px;top:505px;font-size:19px;font-weight:500">Messe 2019</h2>
    <div class="abs c" style="left:384px;top:545px;width:200px;font-size:14px;font-weight:500;color:var(--teal);line-height:1">Tramwash Forum</div>
    <p class="abs small c" style="left:275px;top:606px;width:418px">Lorem ipsum dolor sit amet, consetetur sadipscing elitr, sed diam nonumy eirmod tempor invidunt ut labore et dolore magna aliquyam erat, sed diam voluptua. At vero eos et accusam et justo duo dolores et ea rebum. Stet clita kasd gubergren, no sea takimata sanctus est Lorem ipsum dolor sit amet. Lorem ipsum dolor sit amet, consetetur sadipscing elitr, sed diam nonumy eirmod tempor invidunt ut labore et dolore magna aliquyam erat, sed diam voluptua. At vero eos et accusam et justo duo dolores et ea rebum. Stet clita kasd gubergren, no sea takimata sanctus est Lorem ipsum dolor sit amet.</p>
    <div role="img" aria-label="Nahaufnahme eines gelben Reinigungsschwamms" class="abs" style="left:274px;top:709px;width:132px;height:88px;background:radial-gradient(circle,#f3e45a,#c9b51e)"></div>
    <div role="img" aria-label="Innenraum eines Zugabteils mit Sitzen" class="abs" style="left:417px;top:709px;width:132px;height:197px;background:linear-gradient(160deg,#8fa0ad,#23282e 60%,#111)"></div>
    <div role="img" aria-label="Moderne Bahnhofshalle mit blauer Glasarchitektur" class="abs" style="left:562px;top:709px;width:131px;height:88px;background:linear-gradient(135deg,#1b4fd1,#9fc4ef 55%,#1b3e9a)"></div>
  </section>

  <!-- Aussteller Infos -->
  <section class="abs" style="left:0;top:935px;width:968px;height:700px">
    <svg class="abs" style="left:0;top:0" width="968" height="700" viewBox="0 0 968 700">
      <defs><linearGradient id="foam" x1="0" y1="0" x2="1" y2="1">
        <stop offset="0" stop-color="#4f97d8"/><stop offset=".35" stop-color="#e7f1f8"/><stop offset=".55" stop-color="#1b5fd0"/><stop offset=".8" stop-color="#dfeaf4"/><stop offset="1" stop-color="#2f74d2"/></linearGradient></defs>
      <path d="M0 37 L968 0 L968 663 L0 700Z" fill="url(#foam)" role="img" aria-label="Blauer Reinigungsschaum als Hintergrundfoto"/>
      <path d="M0 700 C350 693 700 680 968 663 L968 627 C700 652 350 675 0 688Z" fill="var(--orange)"/>
    </svg>
    <h2 class="abs c" style="left:0;width:968px;top:117px;font-size:24px;font-weight:500;color:#1a1a1a">Aussteller Infos</h2>
    <div class="abs c" style="left:274px;top:174px;width:419px;height:239px;background:var(--white)">
      <div style="margin:30px auto 0;width:50px;height:50px;border:2px solid #d6dfe3;border-radius:50%;line-height:46px;font-size:15px">300</div>
      <div style="font-size:9px;margin-top:6px">Aussteller</div>
      <p class="small" style="width:130px;margin:8px auto 0;font-size:6.5px;line-height:12px">Lorem ipsum dolor sit amet, consetetur sadipscing elitr, sed diam nonumy eirmod invidunt ut labore et dolore magna aliquyam erat, sed voluptua. At vero eos et accusam et justo duo dolores et ea rebum.</p>
      <span class="btn" style="margin-top:10px">Besucherliste</span>
    </div>
    <div class="card" style="left:274px;top:423px;width:132px;height:127px;background:var(--slate)">
      <h4>Preise und<br>Konditionen</h4><p>Your content goes here. Edit or remove this text inline or in the module Content settings</p><span class="btn light">mehr erfahren</span></div>
    <div class="card" style="left:417px;top:423px;width:132px;height:203px;background:var(--slate-dark);padding-top:28px">
      <h4>Stand planen</h4><p class="sub">Wie Sie Ihren Stand richtig planen</p><p>Lorem ipsum dolor sit amet, consetetur sadipscing elitr, sed diam nonumy eirmod tempor invidunt, sed diam voluptua</p><span class="btn light">Click Here</span><div class="dots" style="margin-top:12px">•••</div></div>
    <div class="card" style="left:562px;top:423px;width:131px;height:117px;background:linear-gradient(135deg,#27323c,#0f151b)">
      <h4>Der richtige Stand</h4><p>Your content goes here. Edit or remove this text inline or in the module Content settings</p><span class="btn">mehr erfahren</span></div>
  </section>

  <!-- Besucher Infos -->
  <section>
    <h2 class="abs" style="left:169px;top:1708px;font-size:20px;font-weight:500">Besucher Infos</h2>
    <p class="abs small" style="left:169px;top:1748px;width:368px">Lorem ipsum dolor sit amet, consetetur sadipscing elitr, sed diam nonumy eirmod tempor invidunt ut labore et dolore magna aliquyam erat, sed diam voluptua. At vero eos et accusam et justo duo dolores et ea rebum. Stet clita kasd gubergren, no sea takimata sanctus est Lorem ipsum dolor sit amet. Lorem ipsum dolor sit amet, consetetur sadipscing elitr, sed diam nonumy eirmod tempor invidunt ut labore et dolore magna aliquyam erat, sed diam voluptua. At vero eos et accusam et justo duo dolores et ea rebum. Stet clita kasd gubergren, no sea takimata sanctus est Lorem ipsum dolor sit amet.</p>
    <div class="abs c" style="left:600px;top:1710px;width:198px;height:78px;background:var(--orange);padding-top:14px">
      <div style="font-size:19px;font-weight:500;color:#1a1a1a;margin-bottom:6px">Tickets kaufen</div>
      <span class="btn light" style="color:#333">zum Ticket-Shop</span>
    </div>
    <div role="img" aria-label="Illustration eines Gleises in Perspektive" class="abs" style="left:600px;top:1798px;width:198px;height:180px;background:linear-gradient(180deg,#f2f2f2,#bdbdbd)"></div>

    <div class="card" style="left:274px;top:2017px;width:203px;height:168px;background:linear-gradient(160deg,#3a4452,#121820);padding-top:26px">
      <h4 style="font-size:17px;line-height:17px">Unterkunft<br>finden</h4><p style="width:150px;margin:0 auto 8px">Kurze Beschreibung der Firma Lorem ipsum dolor sit amet, consetetur sadipscing elitr, sed diam nonumy eirmod tempor invidunt, sed diam voluptua.</p><span class="btn">Click Here</span><div class="dots" style="margin-top:6px">•••</div></div>
    <div class="card" style="left:274px;top:2198px;width:203px;height:94px;background:var(--slate)">
      <h4>Gastronomie</h4><p>Lorem ipsum dolor sit amet, consetetur sadipscing elitr, sed diam nonumy tempor ut labore elt</p><span class="btn light">mehr erfahren</span></div>
    <div class="abs c" style="left:490px;top:2030px;width:203px">
      <div style="font-size:10px;margin-bottom:4px">Daten &amp; Fakten</div>
      <p class="small" style="font-size:6.5px;line-height:11px">Your content goes here. Edit or remove this text inline or in the module Content settings.</p>
      <span class="btn" style="margin-top:6px">mehr erfahren</span>
    </div>
    <div role="img" aria-label="Foto eines Bahnsteigs mit Gleisen" class="abs c" style="left:490px;top:2118px;width:203px;height:124px;background:linear-gradient(135deg,#6f6f72,#2a2b30 60%,#b8b0a6)">
      <div style="margin-top:38px;font-size:16px;font-weight:500;color:var(--orange)">Geländeplan</div>
      <span class="btn" style="margin-top:6px">mehr erfahren</span>
    </div>
  </section>

  <!-- Kontakt -->
  <section class="abs" style="left:0;top:2381px;width:968px;height:400px">
    <svg class="abs" style="left:0;top:0" width="968" height="400" viewBox="0 0 968 400">
      <path d="M0 0 H968 V350 C650 365 300 380 0 391Z" fill="var(--ice)"/>
      <path d="M0 391 C300 380 650 365 968 350 L968 362 C650 377 300 392 0 400Z" fill="var(--orange)"/>
    </svg>
    <div class="abs" style="left:421px;top:49px;width:70px;height:70px;background:var(--teal);display:flex;align-items:center;justify-content:center"><div class="wordmark" style="font-size:11px">Tramwash<br>Forum</div></div>
    <h2 class="abs" style="left:274px;top:153px;font-size:16px;font-weight:400">Kontakt &amp; Beratung</h2>
    <div class="field" style="left:274px;top:178px;width:203px">Name</div>
    <div class="field" style="left:490px;top:178px;width:203px">Vorname</div>
    <div class="field" style="left:274px;top:211px;width:203px">Telefonnummer</div>
    <div class="field" style="left:490px;top:211px;width:203px">E-Mail-Adresse</div>
    <div class="field" style="left:274px;top:245px;width:419px;height:58px">Nachricht</div>
    <div class="abs" style="left:587px;top:382px"></div>
    <div class="abs" style="left:586px;top:318px;font-size:6px;color:#555">10 + 4 =</div>
    <div class="field" style="left:614px;top:312px;width:20px;height:20px"></div>
    <span class="btn abs" style="left:640px;top:314px;width:53px;text-align:center">absenden</span>
  </section>

  <!-- Presse -->
  <section>
    <h2 class="abs c" style="left:0;width:968px;top:2833px;font-size:20px;font-weight:500">Presse</h2>
    <div class="card" style="left:274px;top:2884px;width:132px;height:126px;background:var(--slate)">
      <h4>Preise und<br>Konditionen</h4><p>Your content goes here. Edit or remove this text inline or in the module Content settings</p><span class="btn light">mehr erfahren</span></div>
    <div class="card" style="left:417px;top:2884px;width:132px;height:201px;background:var(--slate-dark);padding-top:28px">
      <h4>Stand planen</h4><p class="sub">Wie Sie Ihren Stand richtig planen</p><p>Lorem ipsum dolor sit amet, consetetur sadipscing elitr, sed diam nonumy eirmod tempor invidunt, sed diam voluptua</p><span class="btn light">Click Here</span><div class="dots" style="margin-top:12px">•••</div></div>
    <div class="card" style="left:562px;top:2884px;width:131px;height:116px;background:linear-gradient(135deg,#27323c,#0f151b)">
      <h4>Der richtige Stand</h4><p>Your content goes here. Edit or remove this text inline or in the module Content settings</p><span class="btn">mehr erfahren</span></div>

    <h3 class="abs" style="left:103px;top:3114px;font-size:8px;font-weight:500">Messe-Katalog</h3>
    <p class="abs small" style="left:103px;top:3129px;width:761px;font-size:6px;line-height:11px">Sed ut perspiciatis unde omnis iste natus error sit voluptatem accusantium doloremque laudantium, totam rem aperiam, eaque ipsa quae ab illo inventore veritatis et quasi architecto beatae vitae dicta sunt explicabo. Nemo enim ipsam voluptatem quia voluptas sit aspernatur aut odit aut fugit, sed quia consequuntur magni dolores eos qui ratione voluptatem sequi nesciunt. Neque porro quisquam est, qui dolorem ipsum quia dolor sit amet, consectetur, adipisci velit, sed quia non numquam eius modi tempora incidunt ut labore et dolore magnam aliquam quaerat voluptatem. Ut enim ad minima veniam, quis nostrum exercitationem ullam corporis suscipit laboriosam, nisi ut aliquid ex ea commodi consequatur? Quis autem vel eum iure reprehenderit qui in ea voluptate velit esse quam nihil molestiae consequatur, vel illum qui dolorem eum fugiat quo voluptas nulla pariatur?</p>
    <div class="acc" style="top:3210px">Messe-Katalog</div>
    <div class="acc" style="top:3255px">Messe-Katalog</div>
    <div class="acc" style="top:3300px">Messe-Katalog</div>
  </section>

  <!-- Karte -->
  <section class="abs" style="left:0;top:3388px;width:968px;height:175px">
    <div role="img" aria-label="Stadtplan mit Standort des Messegeländes" class="abs" style="inset:0;background:linear-gradient(135deg,#eef0ec,#e3e7e0 50%,#f1efe8)"></div>
    <svg class="abs" style="left:478px;top:72px" width="10" height="14" viewBox="0 0 10 14"><path d="M5 14 C2 9 0 7 0 5 A5 5 0 0 1 10 5 C10 7 8 9 5 14Z" fill="#d93025"/><circle cx="5" cy="5" r="2" fill="#fff"/></svg>
    <div class="abs" style="left:6px;top:6px;width:144px;height:40px;background:var(--white);box-shadow:0 1px 3px rgba(0,0,0,.2);padding:5px 7px;font-size:5px;line-height:7px;color:#333">
      <b>Nordhalle Messe GmbH</b><br>Ausstellungsweg 4, 30100 Musterstadt<br><span style="color:#e09a00">4,2 ★★★★</span> 3.100 Rezensionen<br><span style="color:#1a73e8">Größere Karte ansehen</span>
    </div>
  </section>

  <footer class="abs c" style="left:0;top:3563px;width:968px;height:26px;background:var(--footer);font-size:5px;letter-spacing:1px;color:#666;line-height:26px">DATENSCHUTZERKLÄRUNG · IMPRESSUM</footer>
</main>
</body>
</html>
```